Conservative, Modern and Sharp Builder Business card

Hi there,
We would like to update our existing business card.
I have attached photos of existing business card, logo and van sign.

I would like the business card to also list what we do :
Renovation • New Build • Alteration
Extension • Bathroom • Maintenance.(Seperated by dots)

Contact number : 021 0483 0752
(With that exact spacing)

Ideally when people looking from about 2-3 metres, they know that it is a builder’s business card

Open to suggestions on fonts, layout, style of business card

PLEASE ONLY SUBMIT YOUR BEST OR MAX 3 DESIGNS FOR EACH DESIGNER

Thanks

Industry/Entity Type

Construction. Renovation

Contact Information for Business Card

Details should be the same as the existing card. And addition of what we do.

Requirements
Should not have
• The new business card must not have the same layout as our existing one. Thanks

```html
<!DOCTYPE html>
<html lang="en">
<head>
<meta charset="utf-8">
<title>Kowhai Homes Business Card</title>
<link rel="stylesheet" href="https://fonts.googleapis.com/css2?family=Open+Sans:wght@400;600;700;800&display=swap">
<style>
:root{
  --stage:#959595;
  --card:#252525;
  --shade:#151515;
  --accent:#f3b42a;
  --white:#ffffff;
  --muted:#a9a9a9;
  --icon-ink:#252525;
}
*{margin:0;padding:0;box-sizing:border-box}
html,body{width:1200px;height:1000px;overflow:hidden}
body{background:var(--stage);font-family:"Open Sans",sans-serif;position:relative}
.card{position:absolute;width:615px;height:351px;background:var(--card);border-radius:32px;overflow:hidden;box-shadow:0 18px 40px rgba(0,0,0,.35)}
.card-front{left:293px;top:76px}
.card-back{left:299px;top:473px}
.card-shapes{position:absolute;inset:0;width:615px;height:351px}
.card-shapes polygon{fill:var(--shade)}
.brand-name{color:var(--white);font-weight:700;line-height:1;white-space:nowrap}
.brand-square{display:block;background:var(--accent)}

.front-brand{position:absolute;left:72px;top:150px;width:220px;display:flex;flex-direction:column;align-items:center;gap:18px}
.front-brand .brand-square{width:22px;height:22px}
.front-brand .brand-name{font-size:31px}

.services{position:absolute;left:336px;top:50px;list-style:none}
.services li{color:var(--accent);font-weight:800;font-size:18px;line-height:36px}
.services li::before{content:"• "}

.contact-line{position:absolute;left:0;right:0;top:298px;text-align:center;color:var(--white);font-weight:800;font-size:20px}

.back-brand{position:absolute;left:0;right:0;top:50px;display:flex;align-items:center;justify-content:center;gap:16px}
.back-brand .brand-square{width:24px;height:24px}
.back-brand .brand-name{font-size:36px}

.person{position:absolute;right:327px;top:172px;text-align:right}
.person-name{color:var(--accent);font-weight:700;font-size:27px;line-height:1.1}
.person-role{color:var(--muted);font-size:16px;letter-spacing:.08em;margin-top:6px}

.contacts{position:absolute;left:332px;top:142px;list-style:none}
.contacts li{display:flex;align-items:center;height:31px;color:var(--white);font-size:17px}
.contacts .icon{width:24px;height:24px;border-radius:50%;background:var(--accent);margin-right:7px;display:flex;align-items:center;justify-content:center;flex:none}
.contacts .icon svg{width:14px;height:14px}
</style>
</head>
<body>

<section class="card card-front">
  <svg class="card-shapes" viewBox="0 0 615 351" aria-hidden="true">
    <polygon points="615,115 62,351 228,351 615,126"/>
    <polygon points="3,172 220,262 152,290 3,202"/>
  </svg>
  <div class="front-brand">
    <span class="brand-square"></span>
    <div class="brand-name">Kowhai Homes</div>
  </div>
  <ul class="services">
    <li>RENOVATION</li>
    <li>NEW BUILD</li>
    <li>ALTERATION</li>
    <li>EXTENSION</li>
    <li>BATHROOM</li>
    <li>MAINTENANCE</li>
  </ul>
  <p class="contact-line">Contact number : 021 0483 0752</p>
</section>

<section class="card card-back">
  <svg class="card-shapes" viewBox="0 0 615 351" aria-hidden="true">
    <polygon points="615,106 36,351 215,351 615,117"/>
    <polygon points="0,172 216,262 148,290 0,205"/>
  </svg>
  <div class="back-brand">
    <span class="brand-square"></span>
    <div class="brand-name">Kowhai Homes</div>
  </div>
  <div class="person">
    <div class="person-name">TOMAS FERRER</div>
    <div class="person-role">RESIDENTIAL BUILDER</div>
  </div>
  <ul class="contacts">
    <li><span class="icon"><svg viewBox="0 0 24 24"><path fill="#252525" d="M6.6 10.8a15.1 15.1 0 0 0 6.6 6.6l2.2-2.2a1 1 0 0 1 1-.25 11.4 11.4 0 0 0 3.6.6 1 1 0 0 1 1 1V20a1 1 0 0 1-1 1A17 17 0 0 1 3 4a1 1 0 0 1 1-1h3.5a1 1 0 0 1 1 1c0 1.25.2 2.45.6 3.6a1 1 0 0 1-.25 1z"/></svg></span>021-0483-0752</li>
    <li><span class="icon"><svg viewBox="0 0 24 24"><rect x="3" y="5" width="18" height="14" fill="#252525"/><path d="M3 5l9 7 9-7" fill="none" stroke="#f3b42a" stroke-width="1.8"/></svg></span>kowhaihomes@outlook.com</li>
    <li><span class="icon"><svg viewBox="0 0 24 24" fill="none" stroke="#252525" stroke-width="1.8"><circle cx="12" cy="12" r="9"/><ellipse cx="12" cy="12" rx="4" ry="9"/><path d="M3 12h18M5 7h14M5 17h14"/></svg></span>kowhaihomes.nz</li>
    <li><span class="icon"></span>@kowhaihomes.nz</li>
  </ul>
</section>

</body>
</html>
```